New small software startup needs a web design!

Hi! I need a talented web designer to design the overall visual look & feel & navigation of my website.
Just images and basic HTML of course; this is a website design contest not so much a coding contest (although using PHP for "include()" etc might be good!), although yes I have paid the extra $150 for a "Coded Website"

GENERAL OVERVIEW:
-----------------
My new startup company is very simple - I develop and sell shareware apps for desktop.
The software I develop is low-level system & security, so keep that in mind when designing the look & feel of the website.
My website which you are designing for is for hosting the company and showcasing the software.

So it's not a very complicated website, and has a very basic layout/structure.

Most of the webpages I need you to design will essentially just have "blank content" of course, so you don't need to worry about many technicalities, mostly just the LOOK & FEEL & NAVIGATION.

So as you can probably already imagine, it needs things like:
- Download page
- Shop page where they can click links to purchase
- About page where they can read FAQ/Privacy Policy/Terms Of Use, or Contact me
- Members area for registered users to login, where they can download and get tech support
- a subdirectory for each software application to show each off on its own (eg. /software/app1/index.htm)
- a page where i can offer a one-page summary of my products in different foreign languages

IMPORTANT:
----------
- HTML4 ONLY (no HTML5)
- Must support Firefox, Internet Explorer, and Chrome
- CSS is good, although you dont have to use it if you dont want to or feel it's unnecessary
- NO ACTIVE CONTENT (no Flash or Java etc)
- NO SCRIPTS (no Javascript or VBScript etc)
- The overall type of look/feel i'm after is "CLEAN, PROFESSIONAL, TECHNICAL" (but not overcomplicated)
- You must incorporate the company logo - see Attached file.
(You're free to use Photoshop etc to modify the logo how you see fit, for example to resize its elements, or to change the location of the company name part of it, or to remove part of it, change background/transparency, etc etc)
- Although ive named all files here .HTM i'll actually be using PHP, so feel free to use .PHP names also, but .HTM is fine also
- You're also free to use server-side PHP if you wish, for example to include() files such as footer.htm
- Please use Photoshop for designing the images - i'll naturally be needing all PSD files
- Please only use fonts that can be used commercially. The font we use in our logo is 'Good Times' in case you're wondering, although I'm not suggesting one way or the other to use it or not for the website - just because it looks good in the logo may not necessarily mean it works for the rest of the website. Then again, maybe it does, i dont know.

BASIC WEBSITE DIRECTORY STRUCTURE:
----------------------------------
These are the files you should be sending me. Most of these can just be essentially blank pages in regards to content (or with some "dummy filler" text/images), although most (including most "blanks") will obviously have hyperlinks to other pages.
But obviously each page even the blank ones will still have main menu etc.

In no particular order:
---
/index.htm "Welcome to Quorvanta..."
/books/index.htm "Select a book category..."
/books/cat1/index.htm - List of books in cat1
/books/cat2/index.htm - List of books in cat2
/members.htm Username & pass login page. Also acts as the Unsuccessful page.
/members/index.htm - Successfully logged in
/members/download.htm - Members-only downloads
/members/support.htm - Members-only support (basically just a clone of /about/contact.htm)
/about/index.htm "About Quorvanta..."
/about/contact.htm "Contact Us..."
/about/privacy.htm "Privacy Statement"
/about/termsofuse.htm "Terms of Use"
/about/resellers.htm "Information for Resellers"
/lang/index.htm "Select language..."
/lang/fr/index.htm - French products summary page
/lang/es/index.htm - Spanish products summary page
/software/index.htm "Select a program to find out more about it..."
/software/support.htm "Technical support"
/software/shop.htm "Select a program to buy..."
/software/download.htm "Select a program to download..."
/software/app1/index.htm Main "About" page for Application #1
/software/app1/download.htm - Download page for App 1
/software/app1/features.htm - Features page for App 1
/software/app1/screenshots.htm - Screenshots page for App 1
/software/app1/support.htm - Support page for App 1
/software/app1/purchase.htm - Purchase page for App 1
/software/app2/index.htm (clone of App 1)
/software/app2/download.htm "
/software/app2/screenshots.htm "
/software/app2/support.htm "
/software/app2/purchase.htm "
/misc/footer.htm A footer that all other pages also include() -- see below for details

---

MAIN MENU (available from every page):
Home (/index.htm)
Software (/software/index.htm)
Shop (/software/shop.htm)
Books (/books/index.htm)
Members (/members.htm)
Resellers (/about/resellers.htm)
Support (/software/support.htm)
About (/about/index.htm)

FOOTER (every page) for the smallprint:
"Copyright (C) 2015. All rights reserved."
as well as hyperlinks to "Privacy Policy", "Terms of Use", "Contact"

MEMBERS AREA:
The Members subarea also has an extra submenu:
Home (/members/index.htm)
Download (/members/download.htm)
Support (/members/support.htm)

APPLICATION AREA:
Each Application subarea also has an extra submenu:
Home (/software/app1/index.htm)
Features (/software/app1/features.htm)
Download (/software/app1/download.htm)
Support (/software/app1/support.htm)
Purchase (/software/app1/purchase.htm)
Screenshots (/software/app1/screenshots.htm)

Obviously it would be best to have one single FOOTER.HTM that every other HTM file can link to, rather than having the footer in every file (I'll be using PHP so its easy to "include(footer.htm)")

--
Thankyou for taking on my design challenge, and I wish you best of luck and a great design! :)

Target Market(s)

General users of desktop operating system who use system & security tools

Industry/Entity Type

Computer Software

Coding

Coded - Design and coding required

Number of Pages Required

5+ page

Font styles to use
Serif
Sans Serif

Requirements
Must have
• See project description
Should not have
• See project description

```html
<!DOCTYPE html>
<html lang="en">
<head>
<meta charset="utf-8">
<title>Quorvanta — Software Support</title>
<link href="https://fonts.googleapis.com/css2?family=Open+Sans:wght@400;600;700;800&display=swap" rel="stylesheet">
<style>
:root{
  --blue:#1f8fd3;
  --blue-dark:#1577b6;
  --blue-light:#3fb0ea;
  --ink:#3b4249;
  --muted:#7c858d;
  --rule:#e3e7ea;
  --hero-dark:#2a2f34;
  --hero-mid:#5d656c;
  --footer:#2c3034;
  --footer-deep:#222528;
  --footer-text:#a3a9ae;
  --white:#ffffff;
}
*{margin:0;padding:0;box-sizing:border-box}
html,body{width:855px;height:1200px;overflow:hidden;background:var(--white)}
body{font-family:"Open Sans",Arial,sans-serif;color:var(--ink);position:relative}
.page{position:relative;width:855px;height:1200px;overflow:hidden}

/* header */
.site-header{position:absolute;top:0;left:0;width:855px;height:76px;background:var(--white);border-bottom:1px solid var(--rule)}
.brand{position:absolute;left:26px;top:12px;width:84px;text-align:center}
.brand-mark{display:block;width:26px;height:26px;margin:0 auto 5px;border-radius:50%;background:var(--blue)}
.brand-name{font-size:11px;font-weight:700;letter-spacing:1.6px;color:var(--blue);text-transform:uppercase}
.main-nav{position:absolute;left:240px;top:0;display:flex;height:76px}
.main-nav a{display:block;padding:0 9.5px;line-height:76px;font-size:9.5px;font-weight:600;color:var(--ink);text-decoration:none;text-transform:uppercase;letter-spacing:.4px}
.main-nav a.is-active{color:var(--blue);background:#f4f9fc;border-bottom:3px solid var(--blue);line-height:73px}
.lang-switch{position:absolute;right:16px;top:10px;display:flex;gap:3px}
.lang-switch span{display:block;width:8px;height:6px}
.lang-switch .l1{background:#d43c3c}.lang-switch .l2{background:#e8b92c}.lang-switch .l3{background:#3262b7}

/* hero */
.hero{position:absolute;top:77px;left:0;width:855px;height:316px;overflow:hidden}
.hero-photo{position:absolute;inset:0;background:radial-gradient(ellipse at 72% 75%,#8d959b 0%,var(--hero-mid) 35%,var(--hero-dark) 80%)}
.hero-title{position:absolute;top:84px;width:100%;text-align:center;font-size:50px;line-height:64px;font-weight:700;color:var(--white);letter-spacing:.5px}
.hero-sub{position:absolute;top:160px;width:100%;text-align:center;font-size:20px;line-height:27px;color:var(--white)}
.hero-dots{position:absolute;top:293px;left:0;width:100%;display:flex;justify-content:center;gap:6px}
.hero-dots span{width:6px;height:6px;border-radius:50%;background:rgba(255,255,255,.5)}
.hero-dots span.on{background:var(--white)}

/* services */
.services{position:absolute;top:393px;left:0;width:855px;height:208px;background:linear-gradient(180deg,var(--blue-light),var(--blue-dark))}
.service{position:absolute;top:32px;width:150px;text-align:center;color:var(--white)}
.service-icon{width:38px;height:38px;margin:0 auto 12px;border-radius:50%;background:var(--white);display:flex;align-items:center;justify-content:center}
.service-title{font-size:12px;font-weight:600;letter-spacing:2px;line-height:14px;text-transform:uppercase}
.service-text{margin-top:12px;font-size:7px;line-height:10px;color:rgba(255,255,255,.82)}

/* content */
.section-title{font-size:11.5px;font-weight:700;color:var(--blue);letter-spacing:1.5px;text-transform:uppercase;padding-bottom:8px;border-bottom:1px solid var(--rule)}
.software{position:absolute;top:652px;left:68px;width:378px}
.software-photo{position:absolute;top:34px;left:0;width:150px;height:122px;background:linear-gradient(135deg,#d7dde2,#9ea9b2)}
.software-copy{position:absolute;top:36px;left:166px;width:212px;font-size:7.5px;line-height:11px;color:var(--muted)}
.software-copy p{margin-bottom:9px}
.btn{display:inline-block;background:var(--blue);color:var(--white);font-size:7.5px;font-weight:600;padding:6px 11px;border-radius:2px}
.software .btn{position:absolute;top:150px;left:166px}
.books{position:absolute;top:652px;left:500px;width:286px}
.book{position:absolute;left:0;width:286px;height:66px}
.book-cover{position:absolute;left:0;top:0;width:72px;height:62px;background:linear-gradient(135deg,#bac4cc,#6f7c87)}
.book-title{position:absolute;left:86px;top:0;font-size:10px;font-weight:600;color:var(--blue);letter-spacing:1.5px}
.book-text{position:absolute;left:86px;top:17px;width:200px;font-size:7px;line-height:10px;color:var(--muted)}

/* call to action */
.cta{position:absolute;top:900px;left:0;width:855px;height:50px;background:linear-gradient(180deg,#39aee6,#2193d4);display:flex;align-items:center;justify-content:center;gap:20px;color:var(--white)}
.cta-text{font-size:15.5px}
.cta-text strong{font-weight:700}
.cta .btn{background:var(--footer);padding:7px 12px;font-size:8px}

/* footer */
.site-footer{position:absolute;top:950px;left:0;width:855px;height:205px;background:var(--footer)}
.footer-col{position:absolute;top:30px}
.footer-col h3{font-size:14.5px;font-weight:400;color:var(--white);margin-bottom:14px}
.footer-col p{font-size:7px;line-height:10px;color:var(--footer-text);margin-bottom:8px}
.col-about{left:68px;width:190px}
.col-company{left:313px;width:130px}
.col-contact{left:484px;width:170px}
.col-follow{left:700px;width:110px}
.social{display:flex;align-items:center;gap:8px;margin-bottom:8px;font-size:6.5px;color:var(--footer-text)}
.social span{display:block;width:15px;height:15px;border:1px solid #555b60;background:#373c40}
.footer-bar{position:absolute;top:1155px;left:0;width:855px;height:45px;background:var(--footer-deep);text-align:center;line-height:45px;font-size:7px;color:#7f868b}
.footer-bar .top{position:absolute;right:16px;top:0;color:#7f868b}
</style>
</head>
<body>
<div class="page">

  <header class="site-header">
    <div class="brand"><span class="brand-mark"></span><span class="brand-name">Quorvanta</span></div>
    <nav class="main-nav">
      <a class="is-active">Home</a><a>Software</a><a>Shop</a><a>Books</a><a>Members</a><a>Resellers</a><a>Support</a><a>About</a>
    </nav>
    <div class="lang-switch"><span class="l1"></span><span class="l2"></span><span class="l3"></span></div>
  </header>

  <section class="hero">
    <div class="hero-photo" role="img" aria-label="Photo of a laptop keyboard on a desk in dim grey light"></div>
    <h1 class="hero-title">SOFTWARE SUPPORT</h1>
    <p class="hero-sub">Ensure your computer works correctly<br>right from when you turn it on.</p>
    <div class="hero-dots"><span></span><span class="on"></span><span></span></div>
  </section>

  <section class="services">
    <div class="service" style="left:58px">
      <div class="service-icon"><svg width="20" height="20" viewBox="0 0 20 20"><circle cx="10" cy="10" r="5" fill="none" stroke="#1f8fd3" stroke-width="2.4"/><g stroke="#1f8fd3" stroke-width="2.6"><line x1="10" y1="1" x2="10" y2="4"/><line x1="10" y1="16" x2="10" y2="19"/><line x1="1" y1="10" x2="4" y2="10"/><line x1="16" y1="10" x2="19" y2="10"/></g></svg></div>
      <div class="service-title">Technical<br>Support</div>
      <p class="service-text">Quick help with installs, updates and errors so your tools keep running smoothly every day.</p>
    </div>
    <div class="service" style="left:250px">
      <div class="service-icon"><svg width="20" height="20" viewBox="0 0 20 20" fill="#1f8fd3"><rect x="7" y="2" width="6" height="5"/><rect x="1" y="13" width="6" height="5"/><rect x="13" y="13" width="6" height="5"/><path d="M10 7v3M4 13v-3h12v3" fill="none" stroke="#1f8fd3" stroke-width="1.5"/></svg></div>
      <div class="service-title">Network<br>Solutions</div>
      <p class="service-text">Secure setups for home and office networks with clear advice and careful monitoring tools.</p>
    </div>
    <div class="service" style="left:446px">
      <div class="service-icon"><svg width="20" height="20" viewBox="0 0 20 20"><path d="M10 19s-6-6.5-6-11a6 6 0 0 1 12 0c0 4.5-6 11-6 11z" fill="#1f8fd3"/><circle cx="10" cy="8" r="2.2" fill="#fff"/></svg></div>
      <div class="service-title">Onsite<br>Support</div>
      <p class="service-text">We visit your site to check systems, fix problems and set up security tools on each machine.</p>
    </div>
    <div class="service" style="left:640px">
      <div class="service-icon"><svg width="20" height="20" viewBox="0 0 20 20" fill="none" stroke="#1f8fd3" stroke-width="1.6"><circle cx="10" cy="10" r="8"/><ellipse cx="10" cy="10" rx="3.5" ry="8"/><line x1="2" y1="10" x2="18" y2="10"/></svg></div>
      <div class="service-title">Remote<br>Support</div>
      <p class="service-text">Connect securely and let us solve issues from afar, fast and safe, wherever you happen to be.</p>
    </div>
  </section>

  <section class="software">
    <h2 class="section-title">Software</h2>
    <div class="software-photo" role="img" aria-label="Photo of a laptop showing the software on screen"></div>
    <div class="software-copy">
      <p>Neque porro quisquam est qui dolorem ipsum quia dolor sit amet, consectetur, adipisci velit, sed quia non numquam eius modi tempora.</p>
      <p>Neque porro quisquam est qui dolorem ipsum quia dolor sit amet, consectetur, adipisci velit.</p>
      <p>Neque porro quisquam est qui dolorem ipsum quia dolor sit amet, consectetur, adipisci velit, sed quia non numquam.</p>
    </div>
    <span class="btn">Read More</span>
  </section>

  <section class="books">
    <h2 class="section-title">Recetn Books</h2>
    <div class="book" style="top:34px">
      <div class="book-cover" role="img" aria-label="Photo of a computer book cover"></div>
      <div class="book-title">LOREM IPSUM</div>
      <p class="book-text">Neque porro quisquam est qui dolorem ipsum quia dolor sit amet, consectetur.</p>
    </div>
    <div class="book" style="top:114px">
      <div class="book-cover" role="img" aria-label="Photo of a computer book cover"></div>
      <div class="book-title">LOREM IPSUM</div>
      <p class="book-text">Neque porro quisquam est qui dolorem ipsum quia dolor sit amet, consectetur.</p>
    </div>
  </section>

  <section class="cta">
    <p class="cta-text">Get <strong>FREE MONTH</strong> of online technical support <strong>24/7</strong></p>
    <span class="btn">READ MORE</span>
  </section>

  <footer class="site-footer">
    <div class="footer-col col-about">
      <h3>About Us</h3>
      <p>Quorvanta builds small, careful system and security tools for desktop users, made to stay light, fast and easy to trust.</p>
      <p>Neque porro quisquam est qui dolorem ipsum quia dolor sit amet.</p>
    </div>
    <div class="footer-col col-company">
      <h3>Company</h3>
      <p>Privacy Policy<br>Terms of Use<br>Contact</p>
    </div>
    <div class="footer-col col-contact">
      <h3>Contact us</h3>
      <p>18 Harbor Lane, Westfield<br>Open Monday to Friday</p>
      <p>+1 555 014 2270<br>hello@quorvanta.com</p>
    </div>
    <div class="footer-col col-follow">
      <h3>Follow us</h3>
      <div class="social"><span></span>Chatterly</div>
      <div class="social"><span></span>Postwave</div>
      <div class="social"><span></span>Linkroom</div>
    </div>
  </footer>
  <div class="footer-bar">Copyright © 2015 Quorvanta. All rights reserved.<span class="top">▲</span></div>

</div>
</body>
</html>
```